Business Card (double-sided) and Stationary Design for dental office

1) Business Card Design: We need a business card design for a dental specialty office.
Texts should contain:
The name of our office "Bayhaven Grins Orthodontics"
Tagline: "Specialist in Orthodontic and Maxillofacial Orthopedics"
Tag line: "Creating "Talvering" smiles for Children and Adults"
Doctor name: "Doctor Name"
Office Address:
"123 Street Name
City, State Zip code"
Office email address: office@bayhavengrins.com
Website: www.bayhavengrins.com

We will provide the full office address once the design is selected
Theme: beach, paradise, coastal, wave
We would like to have some creativity in design. Some acceptable ideas: front page: logo and office name. Back page: more detail information, and map to office in form of an island. Please see sample from our other location, but you DON'T HAVE TO USE OR COPY THE SAME CONCEPT.

IF POSSIBLE, PLEASE SUBMIT AT LEAST TWO CONCEPTS: ONE WITH THE BACK LOOKING SIMILAR TO WHAT IS IN THE SAMPLE, AND ONE DIFFERENT.

Color: designer to choose. We have different shade of blues and sand color in our office. Please see logo.

2) Please also design a matching set of stationary that compliment the business card and our logo.

Target Market(s)

Dental

Contact Information for Business Card

See descriptions

Font styles to use
Other font styles liked:
• Matching texts in logo

Colors
0054AA
0677BA
7BADD7
CADEEF
E8F1F8
0094D4
00A9DD
6FCCEA
C7EBF8
E9F6FB
00AB8E
00BBA5
67D7C9
C6EFE9
E9F9F6

Requirements
Must have
• Double-sided
Nice to have
• Beach coastal theme
Should not have
• Any shape or drawing of of tooth or teeth. We don’t need these. You don't necessarily have to just cut and paste the logo art and text as a whole, you have the liberty to rearrange the text.

```html
<!DOCTYPE html>
<html lang="en">
<head>
<meta charset="utf-8">
<title>Bayhaven Grins Orthodontics – Business Card</title>
<link rel="stylesheet" href="https://fonts.googleapis.com/css2?family=Montserrat:wght@500;600&family=Poppins:wght@400;500;700&display=swap">
<style>
  :root {
    --brand-blue: #0392d6;
    --map-tint: #2aa3dc;
    --white: #ffffff;
    --text-grey: #7a7a7a;
    --page-bg: #e9e9eb;
  }
  * { margin: 0; padding: 0; box-sizing: border-box; }
  html, body { width: 1200px; height: 1200px; overflow: hidden; }
  body { background: var(--page-bg); position: relative; font-family: "Poppins", sans-serif; }

  .card { position: absolute; left: 181px; width: 917px; height: 523px; overflow: hidden; }
  .card-front { top: 25px; background: var(--brand-blue); }
  .card-back { top: 645px; background: var(--white); }

  .world-map {
    position: absolute; border-radius: 40px;
    background: radial-gradient(ellipse at center, rgba(60,170,225,0.55), rgba(3,146,214,0) 70%);
  }
  .card-front .world-map { left: 20px; top: 40px; width: 880px; height: 470px; }
  .card-back .world-map { left: 20px; top: 0; width: 880px; height: 216px; }

  .brand-mark {
    position: absolute; left: 324px; top: 83px; width: 266px; height: 266px;
    border-radius: 50%; background: var(--white);
  }
  .brand-name {
    position: absolute; left: 0; right: 0; top: 361px; text-align: center;
    color: var(--white); font-weight: 500; font-size: 42px; line-height: 42px; letter-spacing: 1px;
    white-space: nowrap;
  }
  .brand-tagline {
    position: absolute; left: 0; right: 0; top: 411px; height: 14px;
    display: flex; justify-content: center; align-items: center; gap: 8px;
    color: var(--white); font-weight: 500; font-size: 14px; line-height: 14px; letter-spacing: 1.4px;
    white-space: nowrap;
  }
  .brand-tagline .rule { width: 22px; height: 4px; background: var(--white); }

  .back-header { position: absolute; left: 0; top: 0; width: 100%; height: 216px; background: var(--brand-blue); }
  .holder-name {
    position: absolute; left: 0; right: 0; top: 34px; text-align: center;
    font-family: "Montserrat", sans-serif; font-weight: 500; font-size: 52px;
    letter-spacing: 2px; color: var(--white); white-space: nowrap;
  }
  .holder-role {
    position: absolute; left: 351px; top: 118px; width: 201px; height: 43px;
    background: var(--white); color: var(--brand-blue);
    font-weight: 700; font-size: 21px; letter-spacing: 1.5px;
    display: flex; align-items: center; justify-content: center;
  }

  .contact { position: absolute; white-space: nowrap; }
  .contact-icon { position: absolute; left: 0; top: 7px; width: 30px; height: 30px; }
  .contact-label { margin-left: 48px; color: var(--brand-blue); font-size: 30px; letter-spacing: 1.5px; line-height: 42px; }
  .contact-value { margin-left: 48px; margin-top: 2px; color: var(--text-grey); font-size: 25px; letter-spacing: 1px; line-height: 33px; }
  .contact-phone { left: 21px; top: 250px; }
  .contact-address { left: 480px; top: 250px; }
  .contact-email { left: 21px; top: 384px; }
  .contact-web { left: 480px; top: 384px; }
  .contact-email .contact-value, .contact-web .contact-value { margin-top: -4px; }

  .footer-band {
    position: absolute; left: 224px; bottom: 0; width: 470px; height: 16px;
    background: var(--brand-blue);
    clip-path: polygon(12px 0, 458px 0, 100% 100%, 0 100%);
  }
</style>
</head>
<body>

  <section class="card card-front">
    <div class="world-map" role="img" aria-label="Faint world map decoration"></div>
    <div class="brand-mark"></div>
    <div class="brand-name">BayhavenGrins</div>
    <div class="brand-tagline"><span class="rule"></span>Pediatric Dentistry &amp; Orthodontics<span class="rule"></span></div>
  </section>

  <section class="card card-back">
    <div class="back-header"></div>
    <div class="world-map" role="img" aria-label="Faint world map decoration"></div>
    <h1 class="holder-name">ELLIOT MARSH</h1>
    <div class="holder-role">SPECIALIST</div>

    <div class="contact contact-phone">
      <svg class="contact-icon" viewBox="0 0 30 30"><circle cx="15" cy="15" r="14" fill="var(--brand-blue)"/><path d="M10 8.5c1-.6 1.8-.3 2.3.6l1 2c.3.7.1 1.3-.5 1.7l-.8.6c.6 1.6 1.8 2.9 3.4 3.6l.6-.8c.4-.6 1-.8 1.7-.5l2 1c.9.5 1.2 1.3.6 2.3-.8 1.4-2.3 1.9-3.8 1.4-3.5-1.2-6.2-3.9-7.3-7.5-.5-1.6.1-3.1 1.1-3.9z" fill="#fff"/></svg>
      <div class="contact-label">Phone number</div>
      <div class="contact-value">+4 750 555 01 23<br>+4 732 555 01 67</div>
    </div>

    <div class="contact contact-address">
      <svg class="contact-icon" viewBox="0 0 30 30"><circle cx="15" cy="15" r="14" fill="var(--brand-blue)"/><path d="M15 6.5c-3.3 0-5.8 2.5-5.8 5.7 0 4 5.8 11 5.8 11s5.8-7 5.8-11c0-3.2-2.5-5.7-5.8-5.7z" fill="#fff"/><circle cx="15" cy="12.3" r="2.2" fill="var(--brand-blue)"/></svg>
      <div class="contact-label">Adress</div>
      <div class="contact-value">Kelton, United kingdom<br>tidewell str. 14</div>
    </div>

    <div class="contact contact-email">
      <svg class="contact-icon" viewBox="0 0 30 30"><rect x="1" y="1" width="28" height="28" rx="4" fill="var(--brand-blue)"/><rect x="7" y="9.5" width="16" height="11" rx="1" fill="none" stroke="#fff" stroke-width="1.8"/><path d="M7.5 10.5l7.5 6 7.5-6" fill="none" stroke="#fff" stroke-width="1.8"/></svg>
      <div class="contact-label">E-mail</div>
      <div class="contact-value">office@bayhavengrins.com</div>
    </div>

    <div class="contact contact-web">
      <svg class="contact-icon" viewBox="0 0 30 30"><circle cx="15" cy="15" r="14" fill="var(--brand-blue)"/><g fill="none" stroke="#fff" stroke-width="1.4"><circle cx="15" cy="15" r="8"/><ellipse cx="15" cy="15" rx="3.5" ry="8"/><path d="M7 15h16M8.2 11h13.6M8.2 19h13.6"/></g></svg>
      <div class="contact-label">web site</div>
      <div class="contact-value">www.bayhavengrins.com</div>
    </div>

    <div class="footer-band"></div>
  </section>

</body>
</html>
```